Ecommerce Website For Printing Company

Zoravquill.com are a print, design and signage company who sell flyers, business cards, posters, brochures and more to customers in the UK.

Our website is outdated and requires a new design using current web styling and mobile functionality.

We require the following pages to be designed;
- Home Page
- Price Page
- Portfolio Page
- Blog
- Content Page

Our competitors in the printing industry are www.brenticade.com, www.hallowmarsh.co.uk, quorelvane.co.uk, www.tambridok.co.uk

We require the website to give a professional image as well as be easy for customers to navigate, understand and find prices.

Target Market(s)

Businesses

Industry/Entity Type

Printing

Number of Pages Required

4 page

Font styles to use
Sans Serif

Colors
33a6d7

Requirements
Must have
• Popular products, latest news/blog, sales from portfolio, newsletter sign up, footer

```html
<!DOCTYPE html>
<html lang="en">
<head>
<meta charset="utf-8">
<title>Zoravquill.com – Home</title>
<link href="https://fonts.googleapis.com/css2?family=Open+Sans:wght@300;400;600;700&display=swap" rel="stylesheet">
<style>
:root{
  --brand:#33a6d7;
  --brand-deep:#1b6fb5;
  --brand-dark:#0f4f8f;
  --accent:#f7941d;
  --ink:#3a3f44;
  --muted:#8a9299;
  --line:#dfe6ea;
  --paper:#ffffff;
  --soft:#f4f7f9;
}
*{box-sizing:border-box;margin:0;padding:0}
html,body{width:1200px;height:2496px;overflow:hidden}
body{font-family:"Open Sans",Arial,sans-serif;color:var(--ink);background:var(--paper)}
.topbar{height:20px;background:var(--soft);border-bottom:1px solid var(--line);display:flex;justify-content:space-between;align-items:center;padding:0 40px;font-size:9px;color:var(--muted)}
.topbar span{margin-right:18px}
.topbar .account span{margin:0 0 0 22px}
.header{height:44px;display:flex;align-items:center;justify-content:space-between;padding:0 40px}
.logo{display:flex;align-items:center;gap:6px;font-weight:700;font-size:17px;color:var(--brand)}
.logo i{width:12px;height:12px;background:var(--brand);display:block}
.nav{display:flex;gap:38px;font-size:11px;font-weight:600}
.nav a{color:var(--ink);text-decoration:none}
.nav a.active{color:var(--brand)}
.hero{height:336px;background:linear-gradient(120deg,var(--brand-dark),var(--brand-deep) 45%,var(--brand));position:relative;color:#fff;padding:90px 0 0 148px}
.hero h1{font-weight:400;font-size:48px;letter-spacing:1px}
.hero p{font-size:14px;margin-top:6px;font-weight:600}
.hero .price{font-size:26px;margin-top:2px;font-weight:400}
.btn{display:inline-block;margin-top:16px;background:var(--accent);color:#fff;font-size:10px;font-weight:700;padding:9px 22px;border-radius:2px}
.hero .devices{position:absolute;right:150px;top:40px;width:420px;height:260px;background:linear-gradient(160deg,#eaf4fb,#9fcbe8 60%,#5d8fb8);border-radius:6px}
.services{display:flex;justify-content:center;gap:64px;padding:52px 0 0}
.service{width:200px;text-align:center}
.service .ring{width:64px;height:64px;border:2px solid var(--brand);border-radius:50%;margin:0 auto 14px;display:flex;align-items:center;justify-content:center}
.service h3{font-size:13px;color:var(--brand);font-weight:600;margin-bottom:8px}
.service p{font-size:9px;line-height:15px;color:var(--muted)}
.band{margin-top:58px;height:400px;background:linear-gradient(180deg,#2f95d0,var(--brand) 60%,#4ab4e0);color:#fff;text-align:center;padding-top:80px}
.band h2{font-weight:300;font-size:56px;letter-spacing:2px}
.band p{width:760px;margin:10px auto 0;font-size:9px;line-height:15px;opacity:.9}
.features{display:flex;justify-content:center;gap:130px;margin-top:40px}
.feature{width:120px;font-size:11px;font-weight:600}
.feature svg{display:block;margin:0 auto 10px}
.gallery{margin-top:8px;height:232px;display:grid;grid-template-columns:1.05fr .95fr 1.3fr 1fr .9fr}
.gallery .shot{height:100%}
.ourwork{background:#2b2f33;color:#fff;display:flex;flex-direction:column;align-items:center;justify-content:center}
.ourwork h4{font-weight:400;font-size:22px}
.ourwork span{font-size:10px;margin-top:8px}
.products{display:grid;grid-template-columns:repeat(4,220px);column-gap:16px;row-gap:48px;justify-content:center;margin-top:140px}
.card{border:2px solid #a9d7ee;padding:8px;height:192px}
.card .thumb{height:150px;background:linear-gradient(150deg,#f6f6ee,#dfe9d8 55%,#c9dbe6)}
.card h5{font-size:10px;font-weight:400;color:var(--brand);margin-top:8px}
.footerline{position:absolute;left:0;right:0;top:2488px;height:8px;background:var(--brand)}
</style>
</head>
<body>
<div class="topbar">
  <div><span>info@zoravquill.com</span><span>0161 555 0192</span></div>
  <div class="account"><span>My Account</span><span>Basket</span><span>Checkout</span><span>Login / Register</span></div>
</div>
<header class="header">
  <div class="logo"><i></i>Zoravquill</div>
  <nav class="nav"><a class="active" href="#">Home</a><a href="#">Price</a><a href="#">Portfolio</a><a href="#">Blog</a><a href="#">Content Page</a></nav>
</header>
<section class="hero">
  <h1>5000 A5 FLYERS</h1>
  <p>PRINTED ON 350GSM GLOSS, FULL COLOUR, DOUBLE SIDED.</p>
  <div class="price">ONLY £96</div>
  <div class="btn">GET STARTED</div>
  <div class="devices" role="img" aria-label="Website shown on desktop, laptop and tablet screens"></div>
</section>
<section class="services">
  <div class="service"><div class="ring"><svg width="30" height="30" viewBox="0 0 30 30" fill="none" stroke="#33a6d7" stroke-width="2"><rect x="4" y="5" width="10" height="20"/><rect x="16" y="5" width="10" height="20"/></svg></div><h3>Flyer Printing</h3><p>Vivid full colour flyers on quality stock, printed fast and delivered to your door across the UK at great prices.</p></div>
  <div class="service"><div class="ring"><svg width="30" height="30" viewBox="0 0 30 30" fill="none" stroke="#33a6d7" stroke-width="2"><path d="M4 6l11 3v16L4 22z M26 6l-11 3v16l11-3z"/></svg></div><h3>Brochure Printing</h3><p>Stapled and folded brochures that present your business clearly, with a choice of sizes, papers and finishes.</p></div>
  <div class="service"><div class="ring"><svg width="30" height="30" viewBox="0 0 30 30" fill="none" stroke="#33a6d7" stroke-width="2"><path d="M4 11l11-5 11 5-11 5z M4 16l11 5 11-5 M4 21l11 5 11-5"/></svg></div><h3>Stationery Printing</h3><p>Letterheads, compliment slips and business cards that keep every piece of your brand looking consistent.</p></div>
  <div class="service"><div class="ring"><svg width="30" height="30" viewBox="0 0 30 30" fill="none" stroke="#33a6d7" stroke-width="2"><path d="M10 5l-6 4 3 5 3-2v13h10V12l3 2 3-5-6-4c-1 3-9 3-10 0z"/></svg></div><h3>Other Printing</h3><p>Posters, banners, signage and printed garments for events, shops and offices, all handled by one team.</p></div>
</section>
<section class="band">
  <h2>PRINTING</h2>
  <p>From a single box of business cards to large runs of catalogues, our presses handle every job with care. We check each file before printing, use quality papers and inks, and dispatch quickly so your print arrives on time, every time, wherever you are.</p>
  <div class="features">
    <div class="feature"><svg width="36" height="36" viewBox="0 0 36 36" fill="#fff"><circle cx="18" cy="13" r="9"/><path d="M12 20l-3 13 5-3 3 4 1-12zM24 20l3 13-5-3-3 4-1-12z"/></svg>Excellent Quality</div>
    <div class="feature"><svg width="36" height="36" viewBox="0 0 36 36" fill="none" stroke="#fff" stroke-width="3"><circle cx="18" cy="19" r="12"/><path d="M18 12v7l5 3M7 6l-3 3M29 6l3 3"/></svg>Work in Time</div>
    <div class="feature"><svg width="36" height="36" viewBox="0 0 36 36" fill="#fff"><path d="M18 3l14 7-14 7-14-7z M4 12l13 7v15L4 27z M32 12l-13 7v15l13-7z"/></svg>Our Delivery</div>
    <div class="feature"><svg width="36" height="36" viewBox="0 0 36 36"><circle cx="18" cy="18" r="15" fill="#fff"/><circle cx="13" cy="15" r="2" fill="#33a6d7"/><circle cx="23" cy="15" r="2" fill="#33a6d7"/><path d="M11 21q7 7 14 0" stroke="#33a6d7" stroke-width="2.5" fill="none"/></svg>Satisfied Customers</div>
  </div>
</section>
<section class="gallery">
  <div class="shot" role="img" aria-label="Printed cups and desk items" style="background:linear-gradient(135deg,#e9e3d6,#b7a98c)"></div>
  <div class="shot" role="img" aria-label="Branded mug and pens" style="background:linear-gradient(135deg,#d5d8da,#3a3d40)"></div>
  <div class="ourwork"><h4>Our work</h4><span>Lorem Ipsum Check</span></div>
  <div class="shot" role="img" aria-label="Stationery set on a desk" style="background:linear-gradient(135deg,#f2f2f2,#9aa0a4)"></div>
  <div class="shot" role="img" aria-label="Business cards in blue" style="background:linear-gradient(135deg,#cfe3ee,#2d7fb8)"></div>
</section>
<section class="products">
  <div class="card"><div class="thumb" role="img" aria-label="A4 letterhead samples"></div><h5>A4 Letterheads</h5></div>
  <div class="card"><div class="thumb" role="img" aria-label="A4 letterhead samples"></div><h5>A4 Letterheads</h5></div>
  <div class="card"><div class="thumb" role="img" aria-label="A4 letterhead samples"></div><h5>A4 Letterheads</h5></div>
  <div class="card"><div class="thumb" role="img" aria-label="A4 letterhead samples"></div><h5>A4 Letterheads</h5></div>
  <div class="card"><div class="thumb" role="img" aria-label="A4 letterhead samples"></div><h5>A4 Letterheads</h5></div>
  <div class="card"><div class="thumb" role="img" aria-label="A4 letterhead samples"></div><h5>A4 Letterheads</h5></div>
  <div class="card"><div class="thumb" role="img" aria-label="A4 letterhead samples"></div><h5>A4 Letterheads</h5></div>
  <div class="card"><div class="thumb" role="img" aria-label="A4 letterhead samples"></div><h5>A4 Letterheads</h5></div>
  <div class="card"><div class="thumb" role="img" aria-label="A4 letterhead samples"></div><h5>A4 Letterheads</h5></div>
  <div class="card"><div class="thumb" role="img" aria-label="A4 letterhead samples"></div><h5>A4 Letterheads</h5></div>
  <div class="card"><div class="thumb" role="img" aria-label="A4 letterhead samples"></div><h5>A4 Letterheads</h5></div>
  <div class="card"><div class="thumb" role="img" aria-label="A4 letterhead samples"></div><h5>A4 Letterheads</h5></div>
  <div class="card"><div class="thumb" role="img" aria-label="A4 letterhead samples"></div><h5>A4 Letterheads</h5></div>
  <div class="card"><div class="thumb" role="img" aria-label="A4 letterhead samples"></div><h5>A4 Letterheads</h5></div>
  <div class="card"><div class="thumb" role="img" aria-label="A4 letterhead samples"></div><h5>A4 Letterheads</h5></div>
  <div class="card"><div class="thumb" role="img" aria-label="A4 letterhead samples"></div><h5>A4 Letterheads</h5></div>
</section>
<div class="footerline"></div>
</body>
</html>
```